Brimvale Crest Homes needs a business card

We need a business card for a new company in Canada, Ontario. Our company is all about luxury contraction homes for our clients. Our product and services are custom projects design. Under the business logo that will be created, we want a slogan that will be a memorable phrase for consumers to remember us to tell their friends and relatives.

Additional infomation
- Teodoro Vanlesky
- President / Ceo
-519.304.7718

Find point what luxury construction products and services can be done

We like to see colors:
- #663300
- and something other colors or color that would attract the client needs and wants

The final design should communicate leads from new or old clients that will grow our empire. Most of all, we try to work among the budget that clients want

NOTE
- we also need an icon for the business (Example: Instagram, Facebook, and Whatsapp icons)
- We want the company name to be remembered easily for clients and our distributors who would get our orders.
- we need an icon on the business cards: Facebook and Instagram.

Thanks,
Brimvale Crest Homes

```html
<!DOCTYPE html>
<html lang="en">
<head>
<meta charset="utf-8">
<title>Brimvale Crest Homes – Business Card</title>
<link href="https://fonts.googleapis.com/css2?family=Cinzel:wght@400;600&family=Crimson+Text:ital,wght@0,400;0,600;1,600&family=Lato:wght@400&display=swap" rel="stylesheet">
<style>
  :root {
    --brown: #663300;
    --brown-deep: #5a2d00;
    --white: #ffffff;
    --paper: #fbfbfb;
    --grey: #c4c4c4;
    --ink: #1d1d1d;
    --stage: #2b2b2b;
  }
  * { margin: 0; padding: 0; box-sizing: border-box; }
  html, body { width: 1200px; height: 900px; overflow: hidden; background: var(--stage); }
  .canvas { position: relative; width: 1200px; height: 900px; }

  .card {
    position: absolute; left: 285px; width: 630px; height: 360px; overflow: hidden;
  }
  .card--front { top: 70px; background: var(--brown); color: var(--white); }
  .card--back { top: 470px; background: var(--paper); }

  /* front */
  .world-map {
    position: absolute; left: 90px; top: 60px; width: 470px; height: 200px;
    background: radial-gradient(ellipse at center, rgba(255,255,255,0.07), rgba(255,255,255,0) 70%);
  }
  .front-art { position: absolute; inset: 0; }
  .brand-name {
    position: absolute; left: 0; right: 0; top: 118px; text-align: center;
    font-family: "Cinzel", serif; font-weight: 400; font-size: 40px; letter-spacing: 1px;
  }
  .brand-banner {
    position: absolute; left: 50%; top: 170px; transform: translateX(-50%);
    background: var(--white); color: var(--brown);
    font-family: "Crimson Text", serif; font-size: 15px; padding: 1px 12px; white-space: nowrap;
  }
  .tagline {
    position: absolute; left: 0; right: 0; top: 198px; text-align: center;
    font-family: "Crimson Text", serif; font-style: italic; font-weight: 600; font-size: 18px;
  }
  .services-label {
    position: absolute; left: 92px; top: 300px;
    font-family: "Crimson Text", serif; font-weight: 600; font-size: 18px; text-decoration: underline;
  }
  .services { position: absolute; top: 250px; list-style: none; font-family: "Crimson Text", serif; font-size: 16px; line-height: 20px; }
  .services--left { left: 250px; }
  .services--right { left: 395px; }
  .services li { display: flex; align-items: center; gap: 7px; }
  .services li::before {
    content: ""; width: 10px; height: 10px; background: var(--white);
    box-shadow: inset 0 0 0 0 transparent;
    background-image: linear-gradient(var(--brown), var(--brown)), linear-gradient(var(--brown), var(--brown));
    background-size: 1.5px 100%, 100% 1.5px; background-position: center; background-repeat: no-repeat;
  }

  /* back */
  .back-art { position: absolute; inset: 0; }
  .brand-block {
    position: absolute; left: 100px; top: 105px; width: 190px; text-align: center;
    font-family: "Crimson Text", serif; font-weight: 600; font-size: 30px; line-height: 1.05; color: var(--brown);
  }
  .divider { position: absolute; left: 318px; top: 60px; width: 1.5px; height: 150px; background: var(--brown); }
  .contact { position: absolute; left: 345px; top: 62px; font-family: "Crimson Text", serif; }
  .contact__name { font-weight: 600; font-size: 21px; color: var(--brown); }
  .contact__role { font-size: 18px; color: var(--ink); margin-top: -2px; }
  .socials { display: flex; gap: 6px; margin-top: 14px; }
  .socials span { width: 20px; height: 20px; border-radius: 50%; background: var(--brown); }
  .phone { display: flex; align-items: center; gap: 10px; margin-top: 12px; font-family: "Lato", sans-serif; font-size: 18px; color: var(--ink); }
  .phone svg { width: 20px; height: 18px; }
</style>
</head>
<body>
<main class="canvas">

  <section class="card card--front" aria-label="Card front">
    <div class="world-map" role="img" aria-label="Faint dotted world map backdrop"></div>
    <svg class="front-art" viewBox="0 0 630 360" aria-hidden="true">
      <path d="M40 200 Q 230 40 560 58 Q 260 70 40 200 Z" fill="var(--white)"/>
      <line x1="80" y1="262" x2="200" y2="222" stroke="var(--white)" stroke-width="1.5"/>
      <line x1="420" y1="222" x2="550" y2="210" stroke="var(--white)" stroke-width="1.5"/>
    </svg>
    <div class="brand-name">Brimvale Crest Homes</div>
    <div class="brand-banner">Home Renovations &nbsp; Custom Project Design</div>
    <div class="tagline">Helping you to find Home of your dreams</div>
    <div class="services-label">Our Services:</div>
    <ul class="services services--left">
      <li>Roofing</li><li>Gutters</li><li>Painting</li>
    </ul>
    <ul class="services services--right">
      <li>Exterior Design</li><li>Attic Ventilation</li><li>Pressure Washing</li>
    </ul>
  </section>

  <section class="card card--back" aria-label="Card back">
    <svg class="back-art" viewBox="0 0 630 360" preserveAspectRatio="none" aria-hidden="true">
      <path d="M0 330 Q 380 300 630 150 L630 360 L0 360 Z" fill="var(--brown)"/>
      <path d="M300 318 Q 500 270 630 150 L630 172 Q 500 280 300 318 Z" fill="var(--grey)"/>
    </svg>
    <div class="brand-block">Brimvale Crest Homes</div>
    <div class="divider"></div>
    <div class="contact">
      <div class="contact__name">Teodoro Vanlesky</div>
      <div class="contact__role">President / Ceo</div>
      <div class="socials" role="img" aria-label="Social media links">
        <span></span><span></span><span></span>
      </div>
      <div class="phone">
        <svg viewBox="0 0 20 18" aria-hidden="true">
          <path d="M2 6 Q10 0 18 6 L16 8 L13 6 L7 6 L4 8 Z" fill="var(--brown)"/>
          <rect x="5" y="8" width="10" height="8" rx="1.5" fill="var(--brown)"/>
        </svg>
        <span>519.304.7718</span>
      </div>
    </div>
  </section>

</main>
</body>
</html>
```